Pathways to Brightmoor Land Ventures

size of the ad - 8”x 10.75" plus 0.25" bleed
I would like an ad for a magazine that will stand out and make people want to read the ad.
The ad should not be crowded and people reading the ad will be able to read the text.
I would like it to be a creative and modern-day design.
the list of topics should not be the focus of the ad.
the text is attached.
If you decide to use people in the ad then please no ladies.
please note that leave over 1 inch for the bottom of the footer

```html
<!DOCTYPE html>
<html lang="en">
<head>
<meta charset="utf-8">
<title>Pathways to Brightmoor Land Ventures – Course Ad</title>
<link href="https://fonts.googleapis.com/css2?family=Barlow+Condensed:wght@300;400;500;700;800&family=Open+Sans:wght@400&display=swap" rel="stylesheet">
<style>
  :root {
    --paper: #ffffff;
    --sky: #9fc9e4;
    --steel: #4f7fa8;
    --deep: #1b2c44;
    --navy: #17338a;
    --navy-glass: rgba(20, 44, 140, 0.82);
    --yellow: #ffdc00;
    --white: #ffffff;
    --black: #000000;
  }
  * { margin: 0; padding: 0; box-sizing: border-box; }
  html, body {
    width: 907px; height: 1200px; overflow: hidden;
    background: var(--paper);
  }
  .ad {
    position: relative; width: 907px; height: 1200px; overflow: hidden;
    font-family: "Barlow Condensed", "Arial Narrow", sans-serif;
  }
  .hero-photo {
    position: absolute; left: 27px; top: 27px; width: 854px; height: 1040px;
    background:
      radial-gradient(ellipse 260px 360px at 650px 420px, #3a4654 0%, rgba(58,70,84,0) 70%),
      linear-gradient(160deg, var(--sky) 0%, #7fa9c8 35%, var(--steel) 60%, var(--deep) 100%);
  }
  .side-panel {
    position: absolute; left: 27px; top: 27px; width: 468px; height: 1040px;
    background: linear-gradient(180deg, rgba(70,130,200,0.55), rgba(40,80,150,0.55));
  }
  .course-label {
    position: absolute; left: 86px; top: 30px; width: 356px; height: 162px;
    background: var(--navy); overflow: hidden;
  }
  .course-label span {
    position: absolute; left: 18px; top: 48px;
    color: var(--yellow); font-weight: 400; font-size: 58px; line-height: 1;
    letter-spacing: -0.5px; white-space: nowrap;
    transform: scaleX(0.8); transform-origin: left top;
  }
  .headline {
    position: absolute; left: 101px; top: 256px; width: 450px;
    color: var(--yellow); font-weight: 800; font-size: 66px; line-height: 0.98;
    text-transform: uppercase; text-shadow: 3px 4px 6px rgba(0,0,0,0.45);
    white-space: nowrap;
    transform: scaleX(0.74); transform-origin: left top;
  }
  .tagline {
    position: absolute; left: 100px; top: 480px;
    color: var(--white); font-weight: 400; font-size: 42px; line-height: 1.1;
    text-shadow: 1px 2px 4px rgba(0,0,0,0.3); white-space: nowrap;
    transform: scaleX(0.88); transform-origin: left top;
  }
  .details {
    position: absolute; left: 86px; top: 633px; width: 356px; height: 434px;
    background: var(--navy-glass);
    color: var(--white);
  }
  .details .line {
    position: absolute; left: 20px; font-size: 22px; line-height: 1; white-space: nowrap;
  }
  .details .place { color: var(--yellow); font-weight: 500; font-size: 28px; }
  .details .sessions { color: var(--yellow); font-size: 20px; }
  .topics-title {
    position: absolute; left: 22px; top: 278px;
    color: var(--yellow); font-weight: 500; font-size: 16px;
  }
  .topics {
    position: absolute; top: 315px; list-style: none;
    font-size: 15.5px; line-height: 18px;
  }
  .topics.left { left: 22px; width: 140px; }
  .topics.right { left: 186px; width: 160px; }
  .footer {
    position: absolute; left: 27px; top: 1067px; width: 854px; height: 107px;
    background: var(--black);
    display: flex; align-items: center; justify-content: center;
  }
  .footer span {
    color: var(--white); font-family: "Open Sans", Arial, sans-serif; font-size: 22px;
  }
</style>
</head>
<body>
<div class="ad">
  <div class="hero-photo" role="img" aria-label="Blue-toned photo of a smiling bearded businessman in a dark suit pointing at a model house, blurred office background"></div>
  <div class="side-panel"></div>

  <div class="course-label"><span>REAL ESTATE COURSE</span></div>

  <h1 class="headline">Pathways to<br>Brightmoor Land<br>Ventures</h1>

  <p class="tagline">Investing In Knowledge is<br>Investing In Opportunities</p>

  <section class="details">
    <p class="line" style="top:30px;"><span class="place">Larkfield</span> <span class="sessions">10 -Tuesday evenings sessions</span></p>
    <p class="line" style="top:62px;">Starting Feb.28</p>
    <p class="line" style="top:87px;">Limited Partial Scholarships</p>
    <p class="line" style="top:137px;">Early Bird Special</p>
    <p class="line" style="top:186px;">For those that started or</p>
    <p class="line" style="top:211px;">would like to go into real estate</p>

    <p class="topics-title">Topics: partial listing</p>
    <ul class="topics left">
      <li>Real estate investment strategies</li>
      <li>Due diligence</li>
      <li>Financing</li>
      <li>Underwriting</li>
      <li>Property management</li>
    </ul>
    <ul class="topics right">
      <li>Real estate Legal basics</li>
      <li>Sourcing deals</li>
      <li>Syndication</li>
      <li>Dealing with brokers</li>
      <li>Tax fundamentals</li>
    </ul>
  </section>

  <footer class="footer"><span>1inch footer</span></footer>
</div>
</body>
</html>
```